Crestline Lending Group Business Cards

We are looking to revamp the current business cards each of our locations uses. We are a lending company that specializes in personal loans, title loans, and tax services. We have locations in New Mexico, Texas, and Oklahoma.

We would like a cleaner, sleeker look while still highlighting what we offer. Title Loans, Personal Loans & Tax Services. We also want to include our referral fee somewhere on the card. We would like to see an English option as well as a Spanish option for the cards.

PLEASE NOTE: Some business cards do not include the employee's name but just the store's location, while others will include both.

These are double-sided business cards, and we would like to see proof if possible. I have included proofs of our current business cards for you to review below, as well as our company logo. Feel free to get creative with the logo, etc! Colors should match the logo; however, you do not need to use all of our logo colors if you don't want to.

```html
<!DOCTYPE html>
<html lang="en">
<head>
<meta charset="utf-8">
<title>Crestline Lending Group – Business Card</title>
<link rel="stylesheet" href="https://fonts.googleapis.com/css2?family=Noto+Serif:wght@400;500;600;700;900&family=Open+Sans:wght@500&display=swap">
<style>
  :root {
    --backdrop: #f5c92e;
    --card: #ffffff;
    --green: #10512f;
    --red: #c1212a;
    --white: #ffffff;
  }
  * { box-sizing: border-box; margin: 0; padding: 0; }
  html, body { width: 1200px; height: 1200px; overflow: hidden; }
  body {
    background: var(--backdrop);
    font-family: "Noto Serif", Georgia, serif;
    position: relative;
  }
  .card {
    position: absolute;
    left: 199px;
    width: 801px;
    height: 536px;
    background: var(--card);
    overflow: hidden;
    box-shadow: 8px 8px 10px rgba(120, 80, 0, 0.35);
  }
  .card--front { top: 48px; }
  .card--back { top: 612px; }
  .card__swoosh { position: absolute; left: 0; top: 0; width: 801px; height: 536px; }

  /* Front */
  .brand {
    position: absolute;
    left: 0; right: 0;
    top: 175px;
    text-align: center;
    color: var(--green);
    font-weight: 500;
    font-size: 56px;
    line-height: 1.1;
    letter-spacing: -0.5px;
  }
  .brand__web {
    position: absolute;
    left: 0; right: 0;
    top: 340px;
    text-align: center;
    color: var(--red);
    font-family: "Open Sans", Arial, sans-serif;
    font-weight: 500;
    font-size: 30px;
  }

  /* Back: contact bars */
  .contact {
    position: absolute;
    left: 0;
    width: 402px;
    background: var(--green);
    border-radius: 0 10px 10px 0;
    color: var(--white);
    font-weight: 700;
    font-size: 21px;
    line-height: 1.4;
    display: flex;
    align-items: center;
    justify-content: flex-end;
    padding-right: 18px;
    gap: 18px;
    text-align: right;
  }
  .contact--phone { top: 50px; height: 53px; }
  .contact--email { top: 123px; height: 53px; }
  .contact--address { top: 196px; height: 76px; font-size: 20px; line-height: 1.5; }
  .contact__icon { width: 34px; height: 34px; flex: none; }

  /* Services */
  .services {
    position: absolute;
    left: 87px;
    top: 290px;
    list-style: none;
  }
  .services__item {
    display: flex;
    align-items: center;
    gap: 16px;
    color: var(--red);
    font-weight: 600;
    font-size: 31px;
    line-height: 47px;
  }
  .services__tick { width: 26px; height: 26px; flex: none; margin-top: 6px; }

  /* Right column */
  .person {
    position: absolute;
    left: 494px;
    top: 50px;
    width: 320px;
    height: 90px;
    background: var(--green);
    border-radius: 14px 0 0 14px;
    color: var(--white);
    padding: 4px 0 0 36px;
  }
  .person__name { font-size: 40px; font-weight: 500; line-height: 1.15; }
  .person__role { font-size: 25px; font-weight: 500; line-height: 1.1; margin-left: 2px; }
  .referral {
    position: absolute;
    left: 494px;
    top: 165px;
    width: 320px;
    height: 65px;
    background: var(--red);
    border-radius: 14px 0 0 14px;
    color: var(--white);
    font-weight: 900;
    font-size: 36px;
    line-height: 65px;
    padding-left: 19px;
  }
  .offer__get {
    position: absolute;
    left: 507px;
    top: 240px;
    color: var(--red);
    font-weight: 900;
    font-size: 76px;
    line-height: 1;
  }
  .offer__upto {
    position: absolute;
    left: 670px;
    top: 248px;
    color: var(--green);
    font-weight: 700;
    font-size: 31px;
    line-height: 35px;
  }
  .offer__amount {
    position: absolute;
    left: 505px;
    top: 308px;
    color: var(--red);
    font-weight: 900;
    font-size: 112px;
    line-height: 1;
    letter-spacing: -2px;
  }
</style>
</head>
<body>

<section class="card card--front" aria-label="Card front">
  <p class="brand">Crestline<br>Lending Group</p>
  <p class="brand__web">www.crestlinelending.com</p>
  <svg class="card__swoosh" viewBox="0 0 801 536" aria-hidden="true">
    <path d="M0 513 Q400 373 801 513 L801 536 L0 536 Z" fill="var(--green)"/>
    <path d="M0 536 Q400 387 801 536 Z" fill="var(--red)"/>
  </svg>
</section>

<section class="card card--back" aria-label="Card back">
  <div class="contact contact--phone">
    <span>(505) 555-1212</span>
    <svg class="contact__icon" viewBox="0 0 34 34" aria-hidden="true">
      <circle cx="17" cy="17" r="16" fill="var(--red)"/>
      <path d="M11 9.5 l3 -1 l2.5 4.5 l-2 1.8 q1.5 3.5 4.7 5 l1.8 -2 l4.5 2.5 l-1 3 q-2 1.7 -5 0.6 q-7 -3 -9.8 -10 q-1 -3 1.3 -4.4 Z" fill="var(--white)"/>
      <path d="M19 9 a6 6 0 0 1 6 6 M19 12 a3 3 0 0 1 3 3" stroke="var(--white)" stroke-width="1.6" fill="none" stroke-linecap="round"/>
    </svg>
  </div>
  <div class="contact contact--email">
    <span>hello@crestlinelending.com</span>
    <svg class="contact__icon" viewBox="0 0 34 34" aria-hidden="true">
      <circle cx="17" cy="17" r="16" fill="var(--red)"/>
      <rect x="8" y="11" width="18" height="12" fill="var(--white)"/>
      <path d="M8 11 L17 18 L26 11 M8 23 L14 16.5 M26 23 L20 16.5" stroke="var(--red)" stroke-width="1.5" fill="none"/>
    </svg>
  </div>
  <div class="contact contact--address">
    <span>123 Elm street, Suite B,<br>Anytown, Texas 55555</span>
    <svg class="contact__icon" viewBox="0 0 34 34" aria-hidden="true">
      <circle cx="17" cy="17" r="16" fill="var(--red)"/>
      <path d="M17 27 Q10 18.5 10 14.5 a7 7 0 0 1 14 0 Q24 18.5 17 27 Z" fill="var(--white)"/>
      <circle cx="17" cy="14.5" r="2.8" fill="var(--red)"/>
    </svg>
  </div>

  <ul class="services">
    <li class="services__item">
      <svg class="services__tick" viewBox="0 0 26 26" aria-hidden="true"><circle cx="12" cy="14" r="11" fill="var(--green)"/><path d="M6.5 14 l4 4 l13 -14" stroke="var(--white)" stroke-width="2.6" fill="none"/><path d="M18 4 l6 -2" stroke="var(--green)" stroke-width="2"/></svg>
      Title Loans
    </li>
    <li class="services__item">
      <svg class="services__tick" viewBox="0 0 26 26" aria-hidden="true"><circle cx="12" cy="14" r="11" fill="var(--green)"/><path d="M6.5 14 l4 4 l13 -14" stroke="var(--white)" stroke-width="2.6" fill="none"/></svg>
      Tax Services
    </li>
    <li class="services__item">
      <svg class="services__tick" viewBox="0 0 26 26" aria-hidden="true"><circle cx="12" cy="14" r="11" fill="var(--green)"/><path d="M6.5 14 l4 4 l13 -14" stroke="var(--white)" stroke-width="2.6" fill="none"/></svg>
      Personal Loans
    </li>
  </ul>

  <div class="person">
    <p class="person__name">Jane Doe</p>
    <p class="person__role">Branch Manager</p>
  </div>
  <p class="referral">Refer a friend</p>
  <p class="offer__get">GET</p>
  <p class="offer__upto">up<br>to</p>
  <p class="offer__amount">$100</p>

  <svg class="card__swoosh" viewBox="0 0 801 536" aria-hidden="true">
    <path d="M0 513 Q400 373 801 513 L801 536 L0 536 Z" fill="var(--green)"/>
    <path d="M0 536 Q400 387 801 536 Z" fill="var(--red)"/>
  </svg>
</section>

</body>
</html>
```